north lark upkeep services

Target Market(s)

General letter head for emails and letter quotes ect

Colors
0054AA
0677BA
7BADD7
CADEEF
E8F1F8
0094D4
00A9DD
6FCCEA
C7EBF8
E9F6FB

Requirements
Must have
• logo phone email website names
Nice to have
• what we do (from the website)

```html
<!DOCTYPE html>
<html lang="en">
<head>
<meta charset="utf-8">
<title>North Lark Upkeep Services — Letterhead</title>
<link href="https://fonts.googleapis.com/css2?family=Montserrat:wght@500;800&family=Open+Sans:ital,wght@0,400;0,600;1,400&display=swap" rel="stylesheet">
<style>
  :root {
    --brand-deep: #0054AA;
    --brand-mid: #0677BA;
    --brand-soft: #7BADD7;
    --brand-pale: #CADEEF;
    --brand-mist: #E8F1F8;
    --accent-cyan: #00A9DD;
    --ink-navy: #0b3a5c;
    --body-grey: #8fa7b6;
    --paper: #ffffff;
    --backdrop: #e9edf1;
  }
  * { box-sizing: border-box; margin: 0; padding: 0; }
  html, body { width: 1200px; height: 1200px; overflow: hidden; }
  body {
    background: var(--backdrop);
    font-family: "Open Sans", Arial, sans-serif;
  }
  .letter {
    position: absolute;
    left: 160px; top: 30px;
    width: 880px; height: 1140px;
    background: var(--paper);
    box-shadow: 0 4px 18px rgba(0, 40, 80, 0.12);
    overflow: hidden;
  }
  .letter__waves { position: absolute; left: 0; top: 0; width: 880px; height: 1140px; }
  .brand {
    position: absolute; left: 50px; top: 62px;
    display: flex; align-items: center; gap: 16px;
  }
  .brand__dot {
    width: 64px; height: 64px; border-radius: 50%;
    background: var(--brand-deep);
  }
  .brand__name {
    font-family: "Montserrat", Arial, sans-serif;
    font-weight: 800; font-size: 27px; line-height: 1.1;
    color: var(--brand-deep); width: 330px;
  }
  .greeting {
    position: absolute; left: 150px; top: 240px;
    font-style: italic; font-weight: 400; font-size: 38px; color: var(--ink-navy);
  }
  .date {
    position: absolute; right: 122px; top: 262px;
    font-weight: 600; font-size: 20px; color: var(--accent-cyan);
  }
  .letter__body {
    position: absolute; left: 150px; top: 335px; width: 608px;
    font-size: 17px; line-height: 25px; color: var(--body-grey);
    text-align: justify;
  }
  .letter__body p { margin-bottom: 25px; }
  .signature {
    position: absolute; right: 122px; top: 935px; text-align: right;
    color: var(--ink-navy);
  }
  .signature__name { font-size: 22px; font-weight: 400; }
  .signature__role { font-size: 17px; font-weight: 600; margin-top: 8px; }
  .contacts {
    position: absolute; left: 60px; top: 1108px;
    display: flex; gap: 18px; align-items: center;
    font-family: "Montserrat", Arial, sans-serif; font-weight: 500;
    font-size: 12px; color: var(--ink-navy);
  }
  .contact { display: flex; align-items: center; gap: 6px; white-space: nowrap; }
  .contact__icon {
    width: 24px; height: 24px; border-radius: 50%;
    background: var(--brand-deep); color: #fff;
    display: flex; align-items: center; justify-content: center;
    font-size: 13px; font-weight: 800; flex: none;
  }
  .footer-brand {
    position: absolute; right: 40px; top: 1100px;
    font-family: "Montserrat", Arial, sans-serif; font-weight: 800;
    font-size: 15px; line-height: 1.15; color: var(--brand-deep);
    text-align: right; width: 170px;
  }
</style>
</head>
<body>
<main class="letter">
  <svg class="letter__waves" viewBox="0 0 880 1140" aria-hidden="true">
    <defs>
      <linearGradient id="wave" x1="0" x2="1">
        <stop offset="0" stop-color="#0677BA"/>
        <stop offset="1" stop-color="#0054AA"/>
      </linearGradient>
    </defs>
    <path d="M38 190 C 250 120, 480 140, 640 172 C 740 190, 820 175, 860 150 C 800 178, 700 192, 620 180 C 470 158, 250 140, 38 190 Z" fill="url(#wave)"/>
    <path d="M445 112 C 540 90, 620 98, 690 106 C 710 108, 725 104, 732 100 C 700 112, 640 112, 560 102 C 520 98, 480 100, 445 112 Z" fill="url(#wave)"/>
    <path d="M500 145 C 600 120, 720 128, 865 128 C 740 134, 620 132, 500 145 Z" fill="url(#wave)" opacity="0.9"/>
    <g fill="var(--brand-pale)" opacity="0.7">
      <circle cx="525" cy="65" r="24"/><circle cx="605" cy="76" r="15"/>
      <circle cx="687" cy="73" r="24"/><circle cx="787" cy="92" r="36"/>
      <circle cx="84" cy="1025" r="36"/><circle cx="200" cy="1055" r="20"/>
      <circle cx="335" cy="1050" r="33"/><circle cx="490" cy="1055" r="21"/>
      <circle cx="636" cy="1043" r="15"/><circle cx="788" cy="1028" r="23"/>
    </g>
    <path d="M0 1055 C 180 1100, 380 1105, 560 1080 C 700 1060, 800 1055, 890 1062 L 890 1060 C 780 1048, 680 1050, 560 1068 C 380 1092, 180 1085, 0 1048 Z" fill="url(#wave)"/>
  </svg>

  <header class="brand">
    <span class="brand__dot"></span>
    <span class="brand__name">North Lark Upkeep Services</span>
  </header>

  <h1 class="greeting">Dear Mr. Carver,</h1>
  <p class="date">September 20, 2021</p>

  <section class="letter__body">
    <p>Lorem ipsum dolor sit amet, consectetur adipiscing elit. Aliquam congue elit nec justo egestas volutpat. Donec eget metus ut est vestibulum mattis. Suspendisse finibus nisl nulla, ut auctor mauris pellentesque sed. Praesent tincidunt cursus aliquet. Sed in eros non odio maximus sollicitudin.</p>
    <p>Curabitur in vehicula lorem. Ut elit odio, consequat tincidunt nisl ac, tristique faucibus nulla. Sed quis consectetur enim, a porta neque. In dignissim turpis imperdiet risus lacinia, vel lobortis felis faucibus. Curabitur ac mi laoreet, auctor neque sit.</p>
    <p>Vestibulum in nunc congue ex condimentum volutpat. Donec varius nisl erat, nec dapibus elit pharetra gravida. Proin vitae diam semper, congue lorem ut, blandit leo. Aliquam mattis non arcu ac dictum. Vivamus sed neque nunc.</p>
    <p>Suspendisse pharetra consequat est, eu viverra nibh interdum a. Vestibulum fermentum semper diam, ut sollicitudin felis pulvinar sit amet. Aliquam sed risus nec tortor mollis mattis. Morbi bibendum imperdiet malesuada. Aliquam eu urna elizt. Sed porttitor vulputate pellentesque. Duis tempus turpis quis metus vestibulum, ac porttitor dui auctor. Lorem ipsum dolor sit amet.</p>
  </section>

  <div class="signature">
    <p class="signature__name">Dana Whitfield</p>
    <p class="signature__role">Specialist</p>
  </div>

  <footer class="contacts">
    <span class="contact"><span class="contact__icon">@</span>hello@northlarkupkeep.com</span>
    <span class="contact"><span class="contact__icon">
      <svg width="13" height="13" viewBox="0 0 24 24" aria-hidden="true"><path fill="#fff" d="M6.6 10.8a15.1 15.1 0 0 0 6.6 6.6l2.2-2.2c.3-.3.7-.4 1-.2 1.1.4 2.3.6 3.6.6.6 0 1 .4 1 1V20c0 .6-.4 1-1 1C10.6 21 3 13.4 3 4c0-.6.4-1 1-1h3.5c.6 0 1 .4 1 1 0 1.3.2 2.5.6 3.6.1.3 0 .7-.2 1z"/></svg>
    </span>+1-555-014-2290</span>
    <span class="contact"><span class="contact__icon">w</span>www.northlarkupkeep.com</span>
  </footer>
  <p class="footer-brand">North Lark Upkeep Services</p>
</main>
</body>
</html>
```